Real Estate Listing Landing Page

I am looking for a landing page for my Flat Fee MLS Listing website... The name of my website is "Brightkey Home Sales".

I am a big fan of this landing page setup and would like something similar.
https://quaylinehomes.com/

I am a fan of the design style on https://quaylinehomes.com/ and also this design style as well... https://2817.velmontedge.com/

Use your creativity and incorporate your own twists that you would feel lift up this landing pages' appeal. I'd love some red color incorporated within the design.

Target Market(s)

Real Estate Home Sellers

Industry/Entity Type

Real Estate

Coding

Coded - Design and coding required

Font styles to use
Sans Serif

Colors
0054AA
0677BA
7BADD7
CADEEF
E8F1F8
0094D4
00A9DD
6FCCEA
C7EBF8
E9F6FB
EB3D1F
EC4F4E
F09395
F8D3D4
FCEDEE

```html
<!DOCTYPE html>
<html lang="en">
<head>
<meta charset="utf-8">
<title>Brightkey Home Sales – Flat Fee MLS Listings</title>
<link href="https://fonts.googleapis.com/css2?family=Mulish:wght@300;400;600;700&family=Barlow+Condensed:wght@500;600;700&display=swap" rel="stylesheet">
<style>
:root{
  --navy:#1d3a6b;
  --navy-deep:#16325f;
  --blue:#0054aa;
  --band:#2f5a96;
  --orange:#f7a81b;
  --red:#eb3d1f;
  --ink:#1f2d4a;
  --muted:#5e6674;
  --soft:#efeeee;
  --pale:#f4f5f7;
  --line:#c9d4e4;
}
*{box-sizing:border-box;margin:0;padding:0}
html,body{width:1200px;height:3200px;overflow:hidden}
body{font-family:"Mulish",sans-serif;color:var(--ink);background:#fff;position:relative}
h1,h2{font-weight:400}
.abs{position:absolute}
.topbar{left:0;top:0;width:1200px;height:27px;background:var(--navy)}
.topbar-links{right:100px;top:6px;color:#fff;font-size:12px}
.topbar-search{right:88px;top:9px;width:10px;height:10px}
.hero{left:0;top:27px;width:1200px;height:556px;background:linear-gradient(180deg,#fff 0%,#f1f2f4 40%,#e6e8eb 100%)}
.brand{left:141px;top:66px;font-size:20px;font-weight:700;color:var(--navy);display:flex;align-items:center;gap:9px}
.brand-dot{width:16px;height:16px;background:var(--red);border-radius:50%}
.nav{left:421px;top:82px;display:flex;gap:23px;font-size:14.5px;color:var(--navy)}
.nav .hot{color:var(--red)}
.login{left:998px;top:80px;width:71px;height:22px;border:1.5px solid var(--navy);border-radius:3px;font-size:14px;text-align:center;line-height:19px;color:var(--navy)}
.go{left:1092px;top:77px;width:27px;height:27px;border-radius:50%;background:var(--orange)}
.cart{left:1043px;top:38px}
.hero-photo{left:580px;top:155px;width:580px;height:428px;background:linear-gradient(180deg,#eceef1 0%,#a9b4c2 55%,#7d9272 100%)}
.hero-title{left:141px;top:246px;font-size:38px;font-weight:300;line-height:36px;color:var(--navy);letter-spacing:-1px}
.hero-title .accent{font-family:"Barlow Condensed",sans-serif;font-weight:600;color:var(--orange);font-size:40px;letter-spacing:0}
.hero-copy{left:141px;top:338px;width:350px;font-size:16.5px;line-height:24px;color:var(--ink)}
.btn{height:36px;font-family:"Barlow Condensed",sans-serif;font-weight:600;font-size:18px;color:#fff;display:flex;align-items:center;justify-content:center;border-radius:2px}
.btn-list{left:141px;top:439px;width:149px;background:var(--navy)}
.btn-learn{left:301px;top:439px;width:148px;background:var(--orange)}
.tabs{left:302px;top:517px;width:284px;height:59px;background:#fff;border-bottom:2px solid #9aa5b6;font-size:14px;box-shadow:0 6px 18px rgba(0,0,0,.06)}
.tab{position:absolute;top:16px;color:var(--navy)}
.tab.on{color:var(--orange);border-bottom:1px solid var(--orange);padding-bottom:2px}
.search{left:302px;top:576px;width:572px;height:96px;background:#fff;box-shadow:0 10px 24px rgba(0,0,0,.08)}
.field-label{font-size:12px;color:var(--muted);top:24px}
.field-value{font-size:16px;color:var(--navy);top:55px}
.search-btn{left:466px;top:37px;width:80px;height:32px;background:var(--navy);color:#fff;font-size:15px;display:flex;align-items:center;justify-content:center;border-radius:2px}
.plans-photo{left:141px;top:742px;width:186px;height:261px;background:linear-gradient(135deg,#7a3a2a,#b5705a 50%,#d8b29d)}
.plans-title{left:390px;top:739px;font-size:21px;color:var(--navy)}
.plans-list{left:372px;top:798px;list-style:none;font-family:Arial,sans-serif;font-size:14.5px;color:var(--navy)}
.plans-list li{height:23.6px;display:flex;align-items:center;gap:10px}
.tick{width:12px;height:10px}
.more{left:780px;top:966px;width:102px;height:22px;border:1.5px solid var(--navy);border-radius:3px;font-size:13px;text-align:center;line-height:19px;color:var(--navy)}
.reviews{left:0;top:1032px;width:1200px;height:306px;background:var(--soft)}
.reviews-title{left:141px;top:1083px;font-size:25px;line-height:34px;color:var(--navy)}
.quote{left:148px;top:1170px;font-size:12px;line-height:15px;color:#222}
.rule{left:153px;top:1240px;width:59px;height:1px;background:var(--navy)}
.arrow{width:30px;height:28px;border:1.5px solid var(--navy);display:flex;align-items:center;justify-content:center;background:#fff}
.review-photo{left:796px;top:1043px;width:288px;height:269px;background:linear-gradient(160deg,#c9d2dc 0%,#a69f97 45%,#6e655d 100%)}
.review-card{left:573px;top:1150px;width:267px;height:113px;background:#fff;box-shadow:0 8px 20px rgba(0,0,0,.08)}
.avatar{left:27px;top:10px;width:68px;height:58px;border-radius:50%;background:linear-gradient(135deg,#c69b6d,#6c4b32)}
.review-site{left:166px;top:13px;font-size:15px;font-weight:700;color:var(--ink)}
.stars{left:128px;top:62px;display:flex;gap:4px;align-items:center;font-size:15px;font-weight:700;color:var(--navy)}
.saved-photo{left:105px;top:1368px;width:383px;height:434px;background:linear-gradient(170deg,#d9dee4 0%,#5b5d63 40%,#3a3b40 70%,#c07a4a 100%)}
.saved-title{left:570px;top:1469px;font-size:25px;color:var(--navy);letter-spacing:-.5px}
.saved-sub{left:595px;top:1503px;font-size:17px;font-weight:700;color:var(--orange);letter-spacing:.3px}
.amount{left:585px;top:1578px;font-family:"Barlow Condensed",sans-serif;font-size:74px;font-weight:700;color:var(--navy)}
.amount-label{left:586px;top:1660px;font-family:"Barlow Condensed",sans-serif;font-size:22px;font-weight:700;color:var(--ink);letter-spacing:.5px}
.addr{left:598px;top:1689px;font-size:12px;line-height:18px;color:var(--ink)}
.sold{left:594px;top:1742px;font-size:18px;color:var(--ink)}
.steps{left:0;top:1838px;width:1200px;height:627px;background:var(--pale)}
.steps-title{left:0;top:1873px;width:1150px;text-align:center;font-size:24px;color:var(--navy);letter-spacing:-.5px}
.step-line{left:232px;top:1990px;width:671px;height:1.5px;background:#8fa6c3}
.step{width:70px;height:70px;border-radius:50%;background:#fff;border:1.5px solid #8fa6c3;display:flex;align-items:center;justify-content:center;font-size:17px;color:var(--navy);top:1955px}
.step.done{background:var(--navy);border-color:var(--navy)}
.step-label{top:2068px;width:140px;text-align:center;font-size:14px;line-height:15px;color:var(--ink)}
.tip-photo{left:202px;top:2121px;width:742px;height:291px;background:linear-gradient(90deg,#6b5640 0%,#c9a26d 40%,#e4b46a 60%,#4f4a44 100%)}
.tip-card{left:222px;top:2145px;width:268px;height:238px;background:rgba(246,246,246,.93);border-radius:8px}
.tip-title{left:37px;top:34px;font-size:16px;color:var(--navy)}
.tip-copy{left:37px;top:65px;width:200px;font-size:14px;line-height:20.5px;color:var(--muted)}
.tip-next{left:190px;top:212px;font-size:16px;font-weight:600;color:var(--navy)}
.map{left:165px;top:2475px;width:375px;height:235px;background:linear-gradient(180deg,#1c3b86 0%,#1c3b86 62%,#c9c9cc 100%)}
.areas-title{left:623px;top:2476px;font-size:23px;color:var(--navy)}
.areas-copy{left:628px;top:2529px;width:345px;font-size:15.5px;line-height:23.5px;color:var(--navy)}
.loop{left:141px;top:2775px;width:938px;height:185px;background:var(--band)}
.loop-photo{left:99px;top:30px;width:275px;height:155px;background:linear-gradient(180deg,#8a9bb8 0%,#5b6788 60%,#3b4358 100%)}
.loop-title{left:430px;top:47px;font-size:25px;color:#fff}
.loop-sub{left:400px;top:83px;font-size:14px;color:#fff}
.email{left:415px;top:114px;width:410px;height:48px;background:#fff;border-radius:3px}
.email-ph{left:27px;top:14px;font-size:15px;color:var(--ink)}
.email-btn{right:18px;top:9px;width:84px;height:29px;background:var(--navy);color:#fff;font-size:14px;display:flex;align-items:center;justify-content:center;border-radius:3px}
.foot-links{left:218px;top:3033px;font-family:Arial,sans-serif;font-size:12px;color:var(--navy);letter-spacing:-.2px}
.badge{top:3022px;background:#8eaad4;border-radius:3px}
.social{top:3030px;width:18px;height:18px;border-radius:50%;background:var(--navy)}
.bottom{left:0;top:3095px;width:1200px;height:105px;background:var(--navy-deep)}
.copyright{left:294px;top:20px;font-family:Arial,sans-serif;font-size:13px;line-height:19px;color:#fff}
.foot-brand{left:837px;top:22px;font-size:15px;font-weight:700;color:#fff;display:flex;align-items:center;gap:8px}
.foot-brand .brand-dot{width:12px;height:12px}
</style>
</head>
<body>

<div class="abs topbar"></div>
<div class="abs topbar-links">Help Center &nbsp;|&nbsp; Listing Dashboard &nbsp;|</div>
<svg class="abs topbar-search" viewBox="0 0 10 10"><circle cx="4" cy="4" r="3" fill="none" stroke="#fff" stroke-width="1.4"/><line x1="6.2" y1="6.2" x2="9.5" y2="9.5" stroke="#fff" stroke-width="1.4"/></svg>

<section class="abs hero"></section>
<div class="abs hero-photo" role="img" aria-label="Modern high-rise apartment towers with trees and lawn"></div>

<div class="abs brand"><span class="brand-dot"></span>Brightkey Home Sales</div>
<nav class="abs nav">
  <span>How It works</span><span>Pricing</span><span>Why we’re Better ⌄</span><span class="hot">list Your Home ⌄</span><span>Contact Us</span>
</nav>
<svg class="abs cart" width="28" height="24" viewBox="0 0 28 24"><path d="M2 3h5l3 12h13l3-9H9" fill="none" stroke="var(--orange)" stroke-width="2"/><circle cx="12" cy="20" r="2" fill="var(--orange)"/><circle cx="21" cy="20" r="2" fill="var(--orange)"/></svg>
<div class="abs login">Login</div>
<div class="abs go"><svg width="27" height="27" viewBox="0 0 27 27"><path d="M7 13.5h12M14 8.5l5 5-5 5" fill="none" stroke="var(--navy)" stroke-width="2"/></svg></div>

<h1 class="abs hero-title">Selling Your Home With Us<br>Will <span class="accent">Save You Thousands.</span></h1>
<p class="abs hero-copy">Don't pay 6% commission! Our MLS Flat Fee Listing Service lets YOU decide how much you want to pay.l</p>
<div class="abs btn btn-list">LIST YOUR HOME</div>
<div class="abs btn btn-learn">LEARN MORE</div>

<div class="abs tabs">
  <span class="tab" style="left:53px">Buy</span>
  <span class="tab" style="left:130px">Sell</span>
  <span class="tab on" style="left:209px">Rent</span>
</div>
<div class="abs search">
  <span class="abs field-label" style="left:43px">Location</span>
  <span class="abs field-value" style="left:37px">Califorina &nbsp;&nbsp;&nbsp;⌄</span>
  <span class="abs field-label" style="left:181px">Property Type</span>
  <span class="abs field-value" style="left:181px">Most Popular &nbsp;&nbsp;⌄</span>
  <span class="abs field-label" style="left:348px">Price Range</span>
  <span class="abs field-value" style="left:340px">Most Popular</span>
  <div class="abs search-btn">Search</div>
</div>

<div class="abs plans-photo" role="img" aria-label="Red brick building facade with white-framed windows"></div>
<h2 class="abs plans-title">All Plans Include...</h2>
<ul class="abs plans-list">
  <li><svg class="tick" viewBox="0 0 12 10"><path d="M1 5l3.5 3.5L11 1" fill="none" stroke="var(--navy)" stroke-width="2"/></svg>Listing uploaded to sites like HomeScout, NestFinder.com, &amp; more</li>
  <li><svg class="tick" viewBox="0 0 12 10"><path d="M1 5l3.5 3.5L11 1" fill="none" stroke="var(--navy)" stroke-width="2"/></svg>Marketed on the Local MLS, where 92% of Homes are Sold</li>
  <li><svg class="tick" viewBox="0 0 12 10"><path d="M1 5l3.5 3.5L11 1" fill="none" stroke="var(--navy)" stroke-width="2"/></svg>Sell your home and pay NO commission</li>
  <li><svg class="tick" viewBox="0 0 12 10"><path d="M1 5l3.5 3.5L11 1" fill="none" stroke="var(--navy)" stroke-width="2"/></svg>Buyer inquiries are forwarded to you</li>
  <li><svg class="tick" viewBox="0 0 12 10"><path d="M1 5l3.5 3.5L11 1" fill="none" stroke="var(--navy)" stroke-width="2"/></svg>Fast and easy online listing setup process</li>
  <li><svg class="tick" viewBox="0 0 12 10"><path d="M1 5l3.5 3.5L11 1" fill="none" stroke="var(--navy)" stroke-width="2"/></svg>You get all buyer leads</li>
  <li><svg class="tick" viewBox="0 0 12 10"><path d="M1 5l3.5 3.5L11 1" fill="none" stroke="var(--navy)" stroke-width="2"/></svg>You decide buyer’s agent commission</li>
  <li><svg class="tick" viewBox="0 0 12 10"><path d="M1 5l3.5 3.5L11 1" fill="none" stroke="var(--navy)" stroke-width="2"/></svg>We provide all required listing forms &amp; disclosures</li>
</ul>
<div class="abs more">Clik more</div>

<section class="abs reviews"></section>
<h2 class="abs reviews-title">What our Client is saying<br>about our service</h2>
<p class="abs quote">"Brightkey Home Sales puts the power back into the owner's hands<br>and cuts out the middle man saving the seller thousands of dollars!</p>
<div class="abs rule"></div>
<div class="abs arrow" style="left:256px;top:1228px"><svg width="10" height="12" viewBox="0 0 10 12"><path d="M7 1L2 6l5 5" fill="none" stroke="var(--navy)" stroke-width="1.5"/></svg></div>
<div class="abs arrow" style="left:315px;top:1228px"><svg width="10" height="12" viewBox="0 0 10 12"><path d="M3 1l5 5-5 5" fill="none" stroke="var(--navy)" stroke-width="1.5"/></svg></div>
<div class="abs review-photo" role="img" aria-label="Tan stone apartment building against a pale sky"></div>
<div class="abs review-card">
  <div class="abs avatar" role="img" aria-label="Customer photo"></div>
  <div class="abs review-site">ReviewPost</div>
  <div class="abs stars">
    <svg width="84" height="15" viewBox="0 0 84 15"><g fill="var(--orange)"><path id="s" d="M7.5 0l2.2 4.7 5 .6-3.7 3.5 1 5-4.5-2.5L3 13.8l1-5L.3 5.3l5-.6z"/><use href="#s" x="17"/><use href="#s" x="34"/><use href="#s" x="51"/><use href="#s" x="68"/></g></svg>
    4.8
  </div>
</div>

<div class="abs saved-photo" role="img" aria-label="Dark brick building corner with lit windows, viewed from below"></div>
<h2 class="abs saved-title">See How Our Customers Saved</h2>
<div class="abs saved-sub">RECENTLY SOLD PROPERTIES</div>
<div class="abs amount">$480</div>
<div class="abs amount-label">COMMISION SAVED</div>
<p class="abs addr">&nbsp;&nbsp;1420 Harbor Lane, Unit 12<br>Seaside Bay, FL 32000</p>
<div class="abs sold">Sold for: $270,000</div>
<div class="abs arrow" style="left:900px;top:1739px"><svg width="10" height="12" viewBox="0 0 10 12"><path d="M7 1L2 6l5 5" fill="none" stroke="var(--navy)" stroke-width="1.5"/></svg></div>
<div class="abs arrow" style="left:953px;top:1739px"><svg width="10" height="12" viewBox="0 0 10 12"><path d="M3 1l5 5-5 5" fill="none" stroke="var(--navy)" stroke-width="1.5"/></svg></div>

<section class="abs steps"></section>
<h2 class="abs steps-title">Four simple steps to selling your home</h2>
<div class="abs step-line"></div>
<div class="abs step done" style="left:198px"><svg width="34" height="34" viewBox="0 0 34 34"><circle cx="17" cy="17" r="14" fill="none" stroke="#fff" stroke-width="2"/><path d="M10 17l5 5 11-12" fill="none" stroke="#fff" stroke-width="2.4"/></svg></div>
<div class="abs step" style="left:415px"><svg width="30" height="30" viewBox="0 0 30 30" fill="none" stroke="var(--muted)" stroke-width="1.4"><rect x="6" y="4" width="18" height="22"/><path d="M10 10h10M10 14h10M10 18h10M10 22h6"/></svg></div>
<div class="abs step" style="left:644px"><svg width="32" height="32" viewBox="0 0 32 32" fill="none" stroke="var(--muted)" stroke-width="1.4"><rect x="5" y="5" width="18" height="22"/><path d="M9 11h10M9 15h10M9 19h6"/><circle cx="24" cy="22" r="5"/><path d="M21.5 22l2 2 3-3"/></svg></div>
<div class="abs step" style="left:868px">$1000</div>
<div class="abs step-label" style="left:161px">Choose Your<br>Package</div>
<div class="abs step-label" style="left:383px">Complete Online<br>Listing Forms</div>
<div class="abs step-label" style="left:603px">We List You On<br>The Local MLS</div>
<div class="abs step-label" style="left:841px">You Save<br>Thousands</div>

<div class="abs tip-photo" role="img" aria-label="Yellow two-story house with porch and front steps among autumn trees"></div>
<div class="abs tip-card">
  <div class="abs tip-title">How Much Can You Save?</div>
  <p class="abs tip-copy">In addition to listing on the MLS, your home will also be showcased on hundreds of real estate websites that buyers visit when seeking a home.</p>
  <div class="abs tip-next">Next ›</div>
</div>

<div class="abs map" role="img" aria-label="Map of the United States with served states highlighted in navy"></div>
<h2 class="abs areas-title">Service Areas</h2>
<p class="abs areas-copy">MLS Flat Fee Listings are available<br>in all counties of: Alabama, Arkansas, Arizona, California, Connecticut, District of Columbia, Delaware, Florida, Georgia, Iowa, Idaho, Illinois, Indiana, Kansas,</p>

<section class="abs loop">
  <div class="abs loop-photo" role="img" aria-label="Two-story suburban house with garage at dusk"></div>
  <h2 class="abs loop-title">Stay In The Loop</h2>
  <p class="abs loop-sub">Sign-up for our email newsletter for the latest news and listing tips</p>
  <div class="abs email">
    <span class="abs email-ph">Email address*</span>
    <div class="abs email-btn">Sign up Now</div>
  </div>
</section>

<div class="abs foot-links">Refund Policy Web Terms &amp; Conditions Privacy Policy Accessibility Articles/Our Blog Important Letter to Agents</div>
<div class="abs badge" style="left:851px;width:78px;height:32px"></div>
<div class="abs badge" style="left:936px;width:42px;height:42px;top:3018px;background:#3a3a3a"></div>
<div class="abs social" style="left:995px"></div>
<div class="abs social" style="left:1023px"></div>
<div class="abs social" style="left:1053px"></div>

<footer class="abs bottom">
  <p class="abs copyright">Copyright 2023 - Member of the National Home Sellers Guild and Licensed<br>&nbsp;&nbsp;in the following states: Alabama, Arkansas, Arizona, California, Connecticut,</p>
  <div class="abs foot-brand"><span class="brand-dot"></span>Brightkey Home Sales</div>
</footer>

</body>
</html>
```